Aldercrest Chiropractic Rehabilitation and Wellness
Business Card, Portfolio Folder, Stationary, Postcard
Simple
Marlow Tenney
Doctor of Chiropractic
518 Verbena Ridge Avenue
Larkspur Bend, CA 96021
marlow@alderbrook.com
www.alderbrook.com
Fonts are TrajanPro and Corbel
Logo and URL or just logo
Logo
jpg Logo

```html
<!DOCTYPE html>
<html lang="en">
<head>
<meta charset="utf-8">
<title>Aldercrest Chiropractic – Business Cards</title>
<link rel="stylesheet" href="https://fonts.googleapis.com/css2?family=Lato:wght@400;700&display=swap">
<style>
  :root {
    --stage: #5b5753;
    --white: #ffffff;
    --ink: #2b2b2b;
    --blue: #1f74c4;
    --blue-deep: #0b4f9c;
    --blue-light: #3aa0e6;
    --green: #8cc63f;
    --green-light: #a9dc3a;
    --green-deep: #5aa51f;
    --charcoal: #3c3c3e;
    --charcoal-deep: #1f1f21;
    --card-radius: 12px;
  }
  * { box-sizing: border-box; margin: 0; padding: 0; }
  html, body { width: 1200px; height: 851px; overflow: hidden; }
  body { background: var(--stage); font-family: "Lato", sans-serif; position: relative; }

  .card {
    position: absolute;
    width: 463px;
    height: 276px;
    border-radius: var(--card-radius);
    overflow: hidden;
    box-shadow: 0 6px 18px rgba(0,0,0,.35);
  }
  .card--front-light { left: 125px; top: 204px; background: var(--white); }
  .card--front-dark { left: 612px; top: 204px; background: linear-gradient(180deg, #4a4a4c, var(--charcoal)); }
  .card--back-green { left: 125px; top: 497px; background: linear-gradient(160deg, var(--green-light), var(--green-deep)); }
  .card--back-blue { left: 612px; top: 497px; background: linear-gradient(160deg, var(--blue-light), var(--blue-deep)); }

  .swoosh { position: absolute; left: 0; top: 0; width: 463px; height: 276px; }

  .holder { position: absolute; left: 16px; top: 12px; color: var(--white); }
  .holder__name { font-size: 15px; font-weight: 700; }
  .holder__title { font-size: 11px; margin-top: 3px; }

  .contact { position: absolute; left: 16px; top: 190px; font-size: 11.5px; line-height: 1.45; font-style: normal; }
  .card--front-light .contact { color: var(--ink); }
  .card--front-dark .contact { color: var(--white); }

  /* Wordmark: one font, one weight, one colour, plain circle beside it */
  .brand {
    position: absolute;
    display: flex;
    align-items: center;
    gap: 10px;
    font-family: "Lato", sans-serif;
    font-weight: 700;
  }
  .brand__mark { flex: none; width: 34px; height: 34px; border-radius: 50%; background: currentColor; }
  .brand__name { line-height: 1.2; }
  .brand__name-main { display: block; font-size: 18px; }
  .brand__name-sub { display: block; font-size: 10px; }

  .card--front-light .brand { left: 190px; top: 118px; color: var(--blue); }
  .card--front-dark .brand { left: 190px; top: 118px; color: var(--blue-light); }

  .card--back-green .brand,
  .card--back-blue .brand {
    left: 0; right: 0; top: 108px;
    justify-content: center;
    gap: 12px;
    color: var(--white);
  }
  .card--back-green .brand__mark,
  .card--back-blue .brand__mark { width: 44px; height: 44px; }
  .card--back-green .brand__name-main,
  .card--back-blue .brand__name-main { font-size: 24px; }
  .card--back-green .brand__name-sub,
  .card--back-blue .brand__name-sub { font-size: 12px; }
</style>
</head>
<body>

  <section class="card card--front-light">
    <svg class="swoosh" viewBox="0 0 463 276" aria-hidden="true">
      <defs>
        <linearGradient id="band-blue" x1="0" y1="0" x2="1" y2="0">
          <stop offset="0" stop-color="#0b4f9c"/>
          <stop offset="1" stop-color="#3aa0e6"/>
        </linearGradient>
      </defs>
      <path d="M0 0 H463 V48 C360 18 250 104 0 100 Z" fill="url(#band-blue)"/>
      <path d="M0 104 C250 108 360 24 463 54" fill="none" stroke="#8cc63f" stroke-width="3"/>
    </svg>
    <div class="holder">
      <p class="holder__name">Marlow Tenney</p>
      <p class="holder__title">Doctor of Chiropractic</p>
    </div>
    <div class="brand">
      <span class="brand__mark"></span>
      <p class="brand__name"><span class="brand__name-main">Aldercrest Chiropractic</span><span class="brand__name-sub">Rehabilitation and Wellness</span></p>
    </div>
    <address class="contact">
      518 Verbena Ridge Avenue, Larkspur Bend, CA 96021<br>
      Phone : (530) 555 0148<br>
      Email : marlow@alderbrook.com
    </address>
  </section>

  <section class="card card--front-dark">
    <svg class="swoosh" viewBox="0 0 463 276" aria-hidden="true">
      <path d="M0 0 H463 V48 C360 18 250 104 0 100 Z" fill="#1f1f21"/>
      <path d="M0 104 C250 108 360 24 463 54" fill="none" stroke="#3aa0e6" stroke-width="3"/>
    </svg>
    <div class="holder">
      <p class="holder__name">Marlow Tenney</p>
      <p class="holder__title">Doctor of Chiropractic</p>
    </div>
    <div class="brand">
      <span class="brand__mark"></span>
      <p class="brand__name"><span class="brand__name-main">Aldercrest Chiropractic</span><span class="brand__name-sub">Rehabilitation and Wellness</span></p>
    </div>
    <address class="contact">
      518 Verbena Ridge Avenue, Larkspur Bend, CA 96021<br>
      Phone : (530) 555 0148<br>
      Email : marlow@alderbrook.com
    </address>
  </section>

  <section class="card card--back-green">
    <div class="brand">
      <span class="brand__mark"></span>
      <p class="brand__name"><span class="brand__name-main">Aldercrest Chiropractic</span><span class="brand__name-sub">Rehabilitation and Wellness</span></p>
    </div>
  </section>

  <section class="card card--back-blue">
    <div class="brand">
      <span class="brand__mark"></span>
      <p class="brand__name"><span class="brand__name-main">Aldercrest Chiropractic</span><span class="brand__name-sub">Rehabilitation and Wellness</span></p>
    </div>
  </section>

</body>
</html>
```